New webdesign for a cable company

We need a new design for Lumo Nett.

There exist a suggestion for the page, were we have attached files to show you this. The design here is not good enough, but here you can se what content we need.

You can feel free to give adjustment to this design to make it better, our blow us away with a new brilliant design, but from this design you see what content we need.

The important is that the company get a design who represent its products:
- TV = Cable TV
- Bredbånd = Broadband
- Mobil = Mobile phone
- Strøm = Electricity
- Alarm = Alarm
- Lumo Samlet = a cobain pagage of all our products.

Lumo Nett would like costumers who visit the site to het the impression that Lumo Nett is a professional, innovative and fun company.
Updates

We have to day uploaded pictures of the existing page as the link haven't been working for the most of you as it's placed on a server our developer are using and is often shut it down. 

We have also updated the brief with some new and updated description so please read true the updated brief. 

We will at the same time inform that we haven't been able to give feedback on any of the received design and are sorry for that, we will within the next 24 hours hopefully have started responded the different received designs.

Looking forward to see more suggestion and hope you will help us create and very professional and informative design. 

Reason: We have decided to extend the deadline due to the number of design suggestion who is sent in and your lack of response to all designers due to our own workload.

This project was unfortunately for different reason put on ice for a while, but we are now ready to complete the design and will answer and give feedback too all the received design suggestions. 

Within a couple of days we hope we have answered all you who sent us suggestions, we appreciate all suggestions and hope to get in more suggestions.

Reason: Deisgn description have been updated

Target Market(s)

Our costumer are both private and companies

Industry/Entity Type

Tv

Requirements
Must have
• A easy way to promote and inform about changes in our products, there are a constant change in our products and it must bee a easy and good way to changes ass the marked change. Cheek out this link, for a example of what we like/think of here, https://kabel.fjordvisjon.no

On all pages there must be a easy way to click on a order button and too inform about your interest (thats two different things), could be placed in the top right corner for example. In the order form you should follow a step by step part:
1. Cheek what product we can provide you.
2. Chooce products.
3. Costumer inforamtion.
4. Confirmation.

Somewere on the portal it must be possible for costumers to log on to their own administration, where they can cheek for invoices, other statuses, etc.

A main menu existing of:
Hjem (Home)
Produkter (Products)
Storkunde (key account/large costumers)
Kundeservice (Costumerservice)
Min side (My page)

The main menu should have the following sub titles:
- Under "Produkter"/products our different products must be listed
- Under "Kundeservice"/Costumerservice it must have these submenus:
- Hjelp og støtte = Help.
- Faktura = Invoice
- Brukerguider = Userguides
- Abbonementavtaler = Terms and conditions.

A bottom menu where we have 5 main categories, with sub categories:
Om oss (about us)
- Om Lumo Nett (about Lumo Nett)
- Kontaktinformajson ( contact information)
- Pressemeldinger (Pressrelese)
- Ledige stillinger (positions available)
- KRAB ( and organisastion in our field)

Produkter (Product)
- TV (TV)
- Bredbånd (Broadand)
- Telefoni (telephony, both mobil)
- Strøm (elecricity)
- Arlam (Alarm)

Borrettslag/Sameier (Housing cooperatives)
- Løsninger (solutions)
- Produkter (product)
- Kontaktpersoner (contactpersons)

Utbygger (developer)
- Hva vi kan gjøre for dere. (What we can do for you)

Opperatørnett (operators)

Build up the categories and bottom menu something like this:
https://kabel.fjordvisjon.no
www.brenvik.com
Nice to have
• A main menu existing of:
Hjem (Home)
Produkter (Products)
Lumo Nett
Kontakt oss (Contact us)

Under "Produkter"/products our different products must be listed and under "Kundeservice"/Costumerservice it must have these submenus:
- Hjelp og støtte = Help.
- Faktura = Invoice
Should not have
• Any translation section since the homepage only will be in Norwegian.

```html
<!DOCTYPE html>
<html lang="no">
<head>
<meta charset="utf-8">
<title>Lumo Nett</title>
<link href="https://fonts.googleapis.com/css2?family=Source+Sans+3:ital,wght@0,300;0,400;0,500;0,600;1,300;1,400&display=swap" rel="stylesheet">
<style>
:root{
  --page:#efefef;
  --ink:#222;
  --muted:#555;
  --accent:#2ab4e0;
  --accent-dark:#1a97c4;
  --order:#f29a1f;
  --order-dark:#d97f08;
  --black:#000;
  --bar:#e2e2e2;
  --panel:#e6e6e6;
  --footer:#f4f4f4;
  --bottom:#e8e8e8;
}
*{box-sizing:border-box;margin:0;padding:0}
html,body{width:1069px;height:1200px;overflow:hidden}
body{background:var(--page);font-family:"Source Sans 3",sans-serif;color:var(--ink);position:relative}
.abs{position:absolute}
a{color:inherit;text-decoration:none}

.topbar{left:88px;top:0;width:893px;height:93px;background:var(--black);border-radius:0 0 3px 3px}
.brand{left:14px;top:26px;display:flex;align-items:center;gap:10px;color:var(--accent);font-size:34px;font-weight:400}
.brand-dot{width:16px;height:16px;border-radius:50%;background:var(--accent)}
.audience{left:378px;top:0;height:93px;display:flex;font-size:13.5px;color:var(--accent)}
.audience a{display:flex;align-items:center;padding:0 16px;height:93px}
.audience a.active{background:linear-gradient(#2a2a2a,#0c0c0c);width:109px;justify-content:center;padding:0}

.menubar{left:89px;top:93px;width:891px;height:48px;background:linear-gradient(#eee,var(--bar))}
.mainnav{left:34px;top:0;height:48px;display:flex;align-items:center;gap:24px;font-size:14px;font-weight:500;color:#111}
.mainnav .login{display:flex;align-items:center;gap:5px}
.search{left:520px;top:8px;width:180px;height:31px;background:#fff;border-radius:3px;box-shadow:0 0 2px #bbb;font-size:10px;color:#555;padding:9px 14px}
.search svg{position:absolute;right:12px;top:8px}
.actions{left:710px;top:9px;display:flex;gap:6px}
.actions a{height:29px;line-height:29px;padding:0 11px;border-radius:3px;font-size:12.5px;font-weight:600;color:#fff}
.actions .order{background:linear-gradient(var(--order),var(--order-dark))}
.actions .interest{background:linear-gradient(var(--accent),var(--accent-dark))}

.hero{left:89px;top:146px;width:891px;height:402px;border-radius:3px;background:linear-gradient(100deg,#b88a6a 0%,#d8c4b0 35%,#f0ece4 55%,#cdb9a0 80%,#a47a5a 100%)}
.hero-card{left:509px;top:95px;width:345px;height:226px;background:rgba(30,30,30,.85);border-radius:3px;padding:26px 24px;color:#fff}
.hero-card h2{color:var(--accent);font-size:27px;font-weight:400;line-height:1;margin-bottom:20px}
.hero-card p{font-size:14px;line-height:21px}
.btn{display:inline-block;background:linear-gradient(var(--accent),var(--accent-dark));color:#fff;border-radius:3px;text-transform:uppercase}
.hero-card .btn{position:absolute;left:24px;top:170px;width:94px;height:39px;font-size:19px;line-height:39px;text-align:center}
.dots{left:35px;top:356px;display:flex;gap:17px}
.dots span{width:21px;height:21px;border-radius:50%;background:#e8e8e8}
.dots span.on{background:var(--accent)}

h3{font-weight:300;font-style:italic;font-size:20px;text-transform:uppercase;color:#333}
.intro{left:107px;top:569px;width:612px}
.intro p{margin:14px 0 0 3px;font-size:13px;line-height:21.3px;color:var(--muted);font-weight:300}
.intro .btn{margin:14px 0 0 3px;width:76px;height:27px;font-size:11.5px;line-height:27px;text-align:center}

.categories{left:733px;top:561px;width:224px;height:214px;background:var(--panel);border-radius:3px;padding:8px 14px}
.categories h3{padding-bottom:8px;border-bottom:1px solid #fafafa}
.categories ul{list-style:none;margin-top:4px}
.categories li{font-size:13.5px;font-style:italic;font-weight:300;color:#333;height:27px;display:flex;align-items:center;gap:9px}
.categories li::before{content:"";width:8px;height:8px;border-radius:50%;background:#ccc}

.card{top:793px;height:130px;background:#ebebeb;border:1px solid #ddd;border-radius:3px}
.card h3{position:absolute;left:13px;top:8px;font-size:18px}
.card .photo{position:absolute;bottom:0}
.card p{position:absolute;right:12px;top:40px;width:96px;font-size:11px;line-height:13px;color:var(--muted);text-align:justify;font-weight:300}
.card .btn{position:absolute;right:12px;bottom:9px;width:60px;height:20px;font-size:9px;line-height:20px;text-align:center}

.footer{left:0;top:943px;width:1069px;height:194px;background:var(--footer);border-top:1px solid #ddd}
.footer h3{font-size:19px}
.about{left:118px;top:30px;width:270px}
.about p{margin-top:12px;font-size:12.3px;line-height:21.3px;color:var(--muted);font-weight:300}
.products{left:461px;top:30px}
.products ul{list-style:none;margin-top:10px}
.products li{font-size:13px;font-style:italic;font-weight:300;color:#444;line-height:20px}
.products li::before{content:"››";margin-right:10px;color:#777;font-style:normal}
.contact{left:702px;top:30px;width:250px}
.contact .hours{margin-top:10px;font-size:17px;color:#444;font-weight:300}
.phone{display:flex;align-items:center;gap:8px;margin:6px 0 0 10px;font-size:39px;font-weight:600;color:var(--accent);line-height:1}
.mail{margin:6px 0 0 26px;font-size:13px;font-style:italic;color:var(--accent)}

.bottom{left:0;top:1137px;width:1069px;height:63px;background:var(--bottom);border-top:1px solid #fff}
.copy{left:123px;top:21px;font-size:12.3px;color:var(--muted)}
.social{left:851px;top:26px;display:flex;gap:9px}
.social span{width:20px;height:20px;border-radius:2px}
</style>
</head>
<body>

<header class="abs topbar">
  <div class="abs brand"><span class="brand-dot"></span>Lumo Nett</div>
  <nav class="abs audience">
    <a class="active" href="#">Privat kunde</a>
    <a href="#">Sameie og/eller borettslag</a>
    <a href="#">Utbygger</a>
    <a href="#">Bedriftskunde</a>
  </nav>
</header>

<div class="abs menubar">
  <nav class="abs mainnav">
    <a href="#">Hjem</a><a href="#">Produkter</a><a href="#">Storkunde</a><a href="#">Kundeservice</a>
    <a class="login" href="#" aria-label="Min side – logg inn">
      <svg width="11" height="13" viewBox="0 0 11 13"><rect x="0.5" y="5.5" width="10" height="7" rx="1" fill="#111"/><path d="M2.5 5.5V3.8a3 3 0 0 1 6 0v1.7" fill="none" stroke="#111" stroke-width="1.4"/></svg>Min side</a>
  </nav>
  <div class="abs search">Søk
    <svg width="16" height="16" viewBox="0 0 16 16"><circle cx="6.5" cy="6.5" r="5" fill="none" stroke="#888" stroke-width="1.6"/><line x1="10" y1="10" x2="15" y2="15" stroke="#888" stroke-width="2"/></svg>
  </div>
  <div class="abs actions">
    <a class="order" href="#">Bestill</a>
    <a class="interest" href="#">Meld interesse</a>
  </div>
</div>

<section class="abs hero" role="img" aria-label="Photo of a family watching TV together on a sofa, one holding a remote">
  <div class="abs hero-card">
    <h2>LOREM IPSUM IS SIMPLY</h2>
    <p>Sed ut perspiciatis unde omnis iste natus error sit voluptatem accusantium doloremque laudantium, totam rem aperiam, eaque ipsa quae ab illo inven-tore</p>
    <a class="btn" href="#">Videre</a>
  </div>
  <div class="abs dots"><span></span><span></span><span></span><span class="on"></span></div>
</section>

<section class="abs intro">
  <h3>Lumo Nett</h3>
  <p>Sed ut perspiciatis unde omnis iste natus error sit voluptatem accusantium doloremque laudantium, totam rem aperiam, eaque ipsa quae ab illo inventore veritatis et quasi architecto beatae vitae dicta sunt explicabo. Nemo enim ipsam voluptatem quia voluptas sit aspernatur aut odit aut fugit, sed quia consequuntur magni dolores eos qui ratione voluptatem sequi nesciunt. Neque porro quisquam est, qui dolorem ipsum quia dolor sit amet, consectetur, adipisci</p>
  <a class="btn" href="#">Read more</a>
</section>

<aside class="abs categories">
  <h3>Produkter</h3>
  <ul><li>TV</li><li>Bredbånd</li><li>Mobil</li><li>Strøm</li><li>Alarm</li><li>Lumo Samlet</li></ul>
</aside>

<article class="abs card" style="left:107px;width:265px">
  <h3>Lorem ipsum</h3>
  <div class="photo" role="img" aria-label="Photo of a smiling woman holding a laptop" style="left:0;width:150px;height:88px;background:linear-gradient(90deg,#6a4a3a,#d7c8c0 60%,#9aa)"></div>
  <p>But must explain to you how all this mistaken idea of pleasure</p>
  <a class="btn" href="#">Read more</a>
</article>

<article class="abs card" style="left:398px;width:269px">
  <h3 style="top:12px">Lorem ipsum</h3>
  <div class="photo" role="img" aria-label="Flat-screen TV showing a beach scene" style="left:23px;bottom:33px;width:89px;height:62px;background:linear-gradient(#4a8fc8,#bfe3f0 55%,#e8dcc0);border:4px solid #111"></div>
  <p style="top:45px">But must explain to you how all this mistaken idea of pleasure</p>
  <a class="btn" href="#">Read more</a>
</article>

<article class="abs card" style="left:687px;width:269px">
  <h3>Costumerservice</h3>
  <div class="photo" role="img" aria-label="Photo of customer service agents wearing headsets" style="left:0;width:160px;height:95px;background:linear-gradient(90deg,#d8c0a8,#eee 50%,#c8d4e0)"></div>
  <p style="top:45px">But must explain to you how all this mistaken idea of pleasure</p>
  <a class="btn" href="#">Read more</a>
</article>

<footer class="abs footer">
  <div class="abs about">
    <h3>About us</h3>
    <p>Sed ut perspiciatis unde omnis iste natus error sit voluptatem accusantium doloremque laudantium, totam rem aperiam, eaque ipsa quae ab illo inven-tore veritatis et quasi architecto beatae vitae dicta sunt explicabo.</p>
  </div>
  <div class="abs products">
    <h3>Products</h3>
    <ul><li>TV</li><li>Broadband</li><li>Telephony</li><li>Electricity</li><li>Alarm</li></ul>
  </div>
  <div class="abs contact">
    <h3>Contact us</h3>
    <p class="hours">Call us to Time jone : 10:00 -15:00</p>
    <div class="phone">
      <svg width="30" height="32" viewBox="0 0 24 24"><path fill="var(--accent)" d="M6.6 2.2c.6-.4 1.4-.2 1.8.4l2.2 3.4c.4.6.2 1.4-.3 1.8L8.7 9c.9 2.5 3.3 5.3 6.3 6.6l1.3-1.6c.5-.5 1.3-.6 1.8-.2l3.3 2.3c.6.4.7 1.2.3 1.8l-1.5 2.2c-.7 1-2 1.4-3.2 1C9.8 19 4.6 13.4 3.3 6.6 3 5.4 3.5 4.1 4.5 3.5z"/></svg>
      55 12 34 80
    </div>
    <p class="mail">Send via Email : post@lumonett.no</p>
  </div>
</footer>

<div class="abs bottom">
  <p class="abs copy">© 2013.www.lumonett.com</p>
  <div class="abs social"><span style="background:#3b5998"></span><span style="background:#4fc3ec"></span><span style="background:#1a79b5"></span></div>
</div>

</body>
</html>
```